Shopping center investment profile

We need to design a two-page 8.5" x 11" brochure that can be used as a template for profiling our shopping centers and demonstrating our track record to investors.

Our company (KVM Real Estate Investments) owns retail shopping centers in the southwestern United States. Our website is www.kvmtrh.example, but we will be redesigning and modernizing the website and logo in the near future, so please do not use the color schemes or framework of the website for the brochure.

Our investors are institutional and high net worth investors who typically have an existing relationship with our company. They are determining whether to invest multi-millions of dollars in a shopping center opportunity, so the brochure needs to be professional, very high quality and provide key information about the specific property.
Updates

Additional guidance on color scheme:

We would like to see a Blue (something like Hex #5A61BC) and Gold (Hex #EDB215) or (Hex #DDA24B) color scheme with some Black accents 

Thank you!

Target Market(s)

Our target audiences are institutional investors, high net-worth individuals, financial firms and medium to large commercial real estate companies.

Industry/Entity Type

Investment

Requirements
Must have
• Clean and modern look with corresponding fonts and colors.
• Incorporates the information found in the attached "Marlowe Crossing profile" Pages or PDF file.
• Final file design files that can be modified easily
Nice to have
• Two examples of industry brochures are attached. These are examples of the professional quality that we are looking for, not necessarily the design or format.

```html
<!DOCTYPE html>
<html lang="en">
<head>
<meta charset="utf-8">
<title>Marlowe Crossing – Property Profile</title>
<link href="https://fonts.googleapis.com/css2?family=Roboto+Condensed:wght@700&family=Roboto:wght@400&display=swap" rel="stylesheet">
<style>
  :root {
    --blue: #5a5fb2;
    --gold: #edb215;
    --plum: #4f454b;
    --ink: #2b2b2b;
    --white: #ffffff;
    --map-tone: #e6e6e3;
    --sky: #6f9bd6;
    --ground: #5b5660;
  }
  * { box-sizing: border-box; margin: 0; padding: 0; }
  html, body { width: 927px; height: 1200px; overflow: hidden; background: var(--white); }
  body { font-family: "Roboto", Arial, sans-serif; color: var(--ink); }
  .page { position: relative; width: 927px; height: 1200px; overflow: hidden; background: var(--white); }
  .abs { position: absolute; }

  .side-column { left: 0; top: 0; width: 204px; height: 1200px; background: var(--blue); }
  .brand-box { left: 46px; top: 0; width: 158px; height: 160px; background: var(--gold); padding: 36px 0 0 14px; }
  .brand-name { font-family: "Roboto", Arial, sans-serif; font-weight: 400; color: #1d1d1d; line-height: 1; }
  .brand-name .big { display: block; font-size: 54px; letter-spacing: -1px; }
  .brand-name .small { display: block; font-size: 17.5px; line-height: 1.05; margin-top: 4px; }

  .header-band { left: 211px; top: 0; width: 716px; height: 160px; background: var(--blue); }
  .header-corner { right: 0; top: 0; }
  .property-title { left: 252px; top: 38px; color: var(--white); font-family: "Roboto Condensed", Arial, sans-serif; font-weight: 700; }
  .property-title h1 { font-size: 51px; line-height: 1; letter-spacing: -0.5px; }
  .property-title p { font-size: 24px; margin-top: 4px; }
  .profile-tag { right: 29px; top: 30px; text-align: right; font-family: "Roboto Condensed", Arial, sans-serif; font-weight: 700; font-size: 19px; line-height: 1.3; color: #2a2540; }

  .location-map { left: 46px; top: 167px; width: 158px; height: 440px; background: var(--map-tone);
    clip-path: polygon(0 0, 100% 0, 100% 100%, 72% 100%, 0 84%); }
  .property-photo { left: 211px; top: 167px; width: 716px; height: 443px;
    background: linear-gradient(180deg, var(--sky) 0%, #a9c3e6 42%, #c59a77 55%, #9a6a55 68%, var(--ground) 82%, #4c4851 100%); }

  .caption-bar { left: 211px; top: 614px; width: 716px; height: 39px; background: var(--gold);
    clip-path: polygon(0 0, 100% 0, 100% 100%, 24px 100%); display: flex; justify-content: space-between; align-items: center;
    padding: 0 42px 0 48px; font-family: "Roboto Condensed", Arial, sans-serif; font-weight: 700; font-size: 20px; color: #1f1f1f; }

  .detail-panel { left: 535px; top: 653px; width: 392px; height: 547px; background: var(--plum); }
  .section-title { font-family: "Roboto Condensed", Arial, sans-serif; font-weight: 700; font-size: 23px; }

  .summary { left: 239px; top: 700px; width: 272px; }
  .summary .section-title { color: #333; margin-bottom: 22px; }
  .summary table { width: 100%; border-collapse: collapse; font-size: 14.2px; color: #333; }
  .summary td { padding: 5px 0 4px; border-bottom: 1.5px solid #555; vertical-align: top; line-height: 1.25; }
  .summary td:last-child { text-align: right; }

  .highlights { left: 540px; top: 704px; width: 370px; color: var(--white); }
  .highlights .section-title { margin-bottom: 14px; }
  .highlights ul { list-style: none; font-size: 13.4px; line-height: 16.3px; }
  .highlights li { position: relative; padding-left: 17px; }
  .highlights li::before { content: ""; position: absolute; left: 2px; top: 5px; width: 7px; height: 7px; border-radius: 50%; background: var(--white); }
  .results { top: 950px; }

  .side-brand { left: 30px; top: 975px; color: var(--white); }
  .side-brand .brand-name { color: var(--white); }
  .side-brand .big { font-size: 54px; }
  .side-brand .small { font-size: 19px; }
  .office-contact { left: 30px; top: 1095px; color: var(--white); font-size: 12.5px; line-height: 15px; }
</style>
</head>
<body>
<div class="page">
  <div class="abs side-column"></div>
  <svg class="abs" style="left:0;top:0" width="46" height="120" aria-hidden="true"><polygon points="0,0 46,0 46,120 0,40" fill="#fff"/></svg>

  <div class="abs brand-box">
    <div class="brand-name"><span class="big">KVM</span><span class="small">REAL ESTATE<br>INVESTMENTS</span></div>
  </div>

  <div class="abs header-band"></div>
  <svg class="abs header-corner" width="210" height="162" aria-hidden="true">
    <polygon points="0,0 210,0 210,162 170,162" fill="#fff"/>
    <polygon points="18,0 210,0 210,148" fill="var(--gold)"/>
  </svg>
  <div class="abs property-title">
    <h1>Marlowe Crossing</h1>
    <p>Gilbert, Arizona</p>
  </div>
  <div class="abs profile-tag">Property<br>Profile</div>

  <div class="abs location-map" role="img" aria-label="Street map of the area around the shopping center with a location pin"></div>
  <div class="abs property-photo" role="img" aria-label="Rendering of the shopping center storefronts with signage, trees and parking lot"></div>

  <div class="abs caption-bar"><span>Marlowe Crossing, Gilbert, Arizona</span><span>79.490 sq ft</span></div>

  <div class="abs detail-panel"></div>

  <section class="abs summary">
    <h2 class="section-title">Summa</h2>
    <table>
      <tr><td>Property Type</td><td>Shopping Center</td></tr>
      <tr><td>Size</td><td>79,490 sq ft</td></tr>
      <tr><td>79,490 sq ft</td><td>April 2011</td></tr>
      <tr><td>Total Investment</td><td>$X,XXX,XXX</td></tr>
      <tr><td>Purchase Occupancy</td><td>8,39%</td></tr>
      <tr><td>Current Occupancy</td><td>97,29%</td></tr>
      <tr><td>Projected 5-year IRR<br>(Unleveraged)</td><td>XX.XX%</td></tr>
    </table>
  </section>

  <section class="abs highlights">
    <h2 class="section-title">Opportunity</h2>
    <ul>
      <li>Bank owned property with attractive purchase price</li>
      <li>Strong relationship with seller’s broker<br>and decision makers</li>
      <li>Redevelopment upside with management and leasing</li>
      <li>No major renovations required</li>
      <li>Gilbert location has very strong population, education<br>and income demographics</li>
      <li>Adjacent to premier 2,500-residence master planned<br>community of Harbor Reed Lakes</li>
      <li>Strong employment area with the new Eastgate Regional<br>hospital and the adjacent Corwell Cancer center</li>
    </ul>
  </section>

  <section class="abs highlights results">
    <h2 class="section-title">Results</h2>
    <ul>
      <li>Stabilized the shopping center within three years,<br>producing excellent results for investors</li>
      <li>Transformed the center into a vibrant destination<br>that the surrounding community is excited about</li>
      <li>Transitioned legacy tenants to upgrade<br>the business operators</li>
      <li>Reduced the shopping center’s operating expenses<br>by replacing vendors and appealing property taxes</li>
    </ul>
  </section>

  <div class="abs side-brand">
    <div class="brand-name"><span class="big">KVM</span><span class="small">REAL ESTATE<br>INVESTMENTS</span></div>
  </div>
  <address class="abs office-contact" style="font-style:normal">
    480 W Linden Ave Suite 210<br>Mesa, AZ 85210<br>(480) 555-0142
  </address>
</div>
</body>
</html>
```